automatic Real Estate Sales Brochure

Print-out of 3 to 8 pages automatically on a color inkjet printer. Page size A4
All details for my Real Estate Sales Design Project are in attached file.
Here some points:
We have abound 100 real estate objects for sale (houses, flats and pieces of land).
For each item, our system creates automatically a sales documentation, which we print out and hand to the potential buyers after they've visited the object or send it by mail upon request in form of a pdf.
This document should be of 3 to maximum 8 pages.
It should be of a modern design and invite the client to read it.
The information should be clear and quick to find.
If the global look could somehow relate to the look of our web site www.norvelhaus.ch, that would be nice.
The company data is there for legal reasons, but it is the agent's phone and mail that the clients should use for contact.
The photos should be of big size (2 by page?) without being distorted nor cut.
Optionally, to save ink and pages, maybe only the first 3-4 photos full size and the rest smaller?

Target Market(s)

will be printed or sent as PDF "on the fly", meaning no pre-printing at a print shop!

Industry/Entity Type

Real Estate

Font styles to use
Sans Serif

Requirements
Must have
• see details in attached file
Should not have
• no edge-to-edge printing
• no double-page printing (A3)

```html
<!DOCTYPE html>
<html lang="fr">
<head>
<meta charset="utf-8">
<title>Norvelhaus – Dossier de vente</title>
<link href="https://fonts.googleapis.com/css2?family=Roboto+Condensed:wght@400;700&family=Roboto:wght@400;700&display=swap" rel="stylesheet">
<style>
:root{
  --bg:#5d6a5e;
  --page:#f4f4f5;
  --header:#e3e3e6;
  --red:#d6472d;
  --ink:#2a2a2c;
  --dark:#303033;
  --mid:#4a4a4e;
  --grey:#bfbfc3;
  --white:#ffffff;
  --wood:#b9864f;
  --wall:#d9d6d0;
}
*{box-sizing:border-box;margin:0;padding:0}
html,body{width:1200px;height:789px;overflow:hidden;background:var(--bg);font-family:"Roboto",Arial,sans-serif;color:var(--ink)}
.spread{position:absolute;left:70px;top:27px;width:1060px;height:735px;display:flex;gap:20px}
.page{position:relative;width:520px;height:735px;background:var(--page);overflow:hidden;box-shadow:0 6px 18px rgba(0,0,0,.35)}
.brand{display:flex;align-items:center;gap:8px;font-family:"Roboto Condensed",sans-serif;font-weight:700;font-size:32px;color:var(--ink);letter-spacing:.5px}
.brand-mark{width:16px;height:16px;background:var(--red)}
.tagline{font-family:"Roboto Condensed",sans-serif;font-weight:700;font-size:11px;color:var(--mid);margin-top:2px}
.photo{position:absolute;border:3px solid var(--white);box-shadow:0 1px 4px rgba(0,0,0,.3)}
.room{background:linear-gradient(180deg,var(--wall) 0%,#ecebe8 55%,var(--wood) 56%,#8d5e33 100%)}
.bath{background:linear-gradient(180deg,#e9e9ea,#b8b8bb)}
.garden{background:linear-gradient(180deg,#cfdde9 0%,#7d9a5a 40%,#3d5a2a 100%)}
.wardrobe{background:linear-gradient(90deg,#e6d7b5 0%,#2a2a2a 45%,#111 100%)}

/* left page */
.lp-header{position:absolute;left:0;top:0;width:520px;height:110px;background:var(--header);padding:22px 26px}
.lp-title{position:absolute;right:26px;top:38px;text-align:right;font-family:"Roboto Condensed",sans-serif;font-weight:700;font-size:20px;line-height:1.15}
.footer{position:absolute;bottom:0;left:0;width:100%;height:100px}
.agent{position:absolute;left:0;bottom:0;width:250px;height:62px;background:var(--dark);color:var(--white);display:flex;align-items:center;gap:8px;padding:0 16px}
.agent-name{font-family:"Roboto Condensed",sans-serif;font-weight:700;font-size:15px;line-height:1;text-transform:uppercase;border-right:2px solid var(--white);padding-right:8px}
.agent-contact{font-family:"Roboto Condensed",sans-serif}
.agent-mail{font-size:10px}
.agent-phone{font-size:18px;font-weight:700}
.company{position:absolute;right:0;bottom:0;width:270px;height:62px;background:var(--mid);color:var(--white);display:flex;align-items:center;gap:10px;padding:0 14px;font-family:"Roboto Condensed",sans-serif;font-weight:700;font-size:12px;line-height:1.25}
.company .sep{width:2px;height:32px;background:var(--white)}

/* right page */
.rp-photo{position:absolute;left:0;top:0;width:320px;height:330px}
.rp-brand{position:absolute;left:22px;top:18px}
.rp-red{position:absolute;left:320px;top:0;width:200px;height:285px;background:var(--red);color:var(--white);display:flex;align-items:flex-end;justify-content:flex-end;padding:0 18px 26px;text-align:right;font-family:"Roboto Condensed",sans-serif;font-weight:700;font-size:25px;line-height:1.15}
.rp-grey{position:absolute;left:300px;top:285px;width:220px;height:355px;background:var(--grey);padding:24px 18px}
.facts{width:100%;border-collapse:collapse;font-family:"Roboto Condensed",sans-serif;font-size:12px;margin-bottom:34px}
.facts th{text-align:left;font-weight:700;padding:3px 0}
.facts td{text-align:right;border-bottom:1px dashed var(--red);padding:3px 0;color:var(--mid)}
.rp-text{position:absolute;left:0;top:330px;width:300px;height:310px;background:var(--white);padding:22px 22px;font-size:11px;line-height:1.4;text-align:justify}
.rp-text p{margin-bottom:8px}
.rp-footer .agent{width:300px}
.rp-footer .company{width:220px;background:var(--mid)}
</style>
</head>
<body>
<div class="spread">

  <section class="page page-left">
    <header class="lp-header">
      <div class="brand"><span class="brand-mark"></span>norvelhaus</div>
      <div class="tagline">Spécialiste Romand De Vente Immobilière</div>
      <h2 class="lp-title">Lumineux 4.5 de 100m2<br>idéalement situé, 1200 Genève</h2>
    </header>

    <div class="photo room" style="left:26px;top:130px;width:175px;height:140px" role="img" aria-label="Séjour lumineux avec parquet"></div>
    <div class="photo wardrobe" style="left:208px;top:122px;width:150px;height:150px" role="img" aria-label="Chambre avec armoire vitrée noire"></div>
    <div class="photo room" style="left:364px;top:118px;width:130px;height:135px" role="img" aria-label="Pièce vide avec fenêtres"></div>
    <div class="photo room" style="left:26px;top:280px;width:175px;height:160px" role="img" aria-label="Couloir et portes blanches"></div>
    <div class="photo room" style="left:208px;top:280px;width:150px;height:160px" role="img" aria-label="Entrée avec armoires blanches"></div>
    <div class="photo room" style="left:364px;top:262px;width:130px;height:175px" role="img" aria-label="Cuisine ouverte vue du séjour"></div>
    <div class="photo garden" style="left:26px;top:450px;width:240px;height:170px" role="img" aria-label="Jardin arboré"></div>
    <div class="photo bath" style="left:272px;top:446px;width:222px;height:174px" role="img" aria-label="Salle de bains carrelée"></div>

    <footer class="footer">
      <div class="agent">
        <div class="agent-name">Nadia<br>Morel</div>
        <div class="agent-contact"><div class="agent-mail">morel@norvelhaus.ch</div><div class="agent-phone">079 555 21 84</div></div>
      </div>
      <div class="company">
        <div>Norvelhaus Sàrl<br>1804 Corsier</div>
        <span class="sep"></span>
        <div>Web: www.norvelhaus.ch<br>Tél: 021 555 30 66</div>
      </div>
    </footer>
  </section>

  <section class="page page-right">
    <div class="rp-photo room" role="img" aria-label="Séjour avec cuisine ouverte et parquet"></div>
    <div class="rp-brand">
      <div class="brand"><span class="brand-mark"></span>norvelhaus</div>
      <div class="tagline" style="color:var(--white)">Spécialiste Romand De Vente Immobilière</div>
    </div>
    <h1 class="rp-red">Lumineux<br>4.5 de 100m2<br>idéalement situé<br>1200 Genève</h1>

    <div class="rp-grey">
      <table class="facts">
        <tr><th>Type de bien</th><td>Appartement</td></tr>
        <tr><th>Surface habitable</th><td>100m2</td></tr>
        <tr><th>Pièces</th><td>4.5</td></tr>
        <tr><th>Surface parcelle</th><td>1'000m2</td></tr>
      </table>
      <table class="facts">
        <tr><th>Prix</th><td>CHF 910'000.-</td></tr>
        <tr><th>Année</th><td>1994</td></tr>
        <tr><th>Etat</th><td>bon état</td></tr>
        <tr><th>Disponible</th><td>à convenir</td></tr>
      </table>
    </div>

    <div class="rp-text">
      <p>Professionnels de l'immobilier, nous avons créé la société Norvelhaus Sàrl en 2006 pour répondre aux attentes spécifiques de notre clientèle romande, nationale et internationale.</p>
      <p>Notre volonté est claire : être VOTRE spécialiste romand du courtage immobilier.</p>
      <p>Pour ceci, chaque courtier réside dans sa région d'action et saura vous conseiller au mieux pour la réalisation de votre projet d'achat ou de vente.</p>
      <p>N'hésitez pas à nous contacter !!!</p>
    </div>

    <footer class="footer rp-footer">
      <div class="agent">
        <div class="agent-name">Nadia<br>Morel</div>
        <div class="agent-contact"><div class="agent-mail">morel@norvelhaus.ch</div><div class="agent-phone">079 555 21 84</div></div>
      </div>
      <div class="company">
        <div>Norvelhaus Sàrl<br>1804 Corsier</div>
        <span class="sep"></span>
        <div>Web: www.norvelhaus.ch<br>Tél: 021 555 30 66</div>
      </div>
    </footer>
  </section>

</div>
</body>
</html>
```